Stationary Design (using existing logo)

Stationary (print and electronic version for Word/email), envelope, and fax cover. All companies are part of same family or course so designs can be the same, or essentially the same. Use the logos attached, same font and colors.

Target Market(s)

Real estate professionals. Investors and other property owners. Financial professionals.

Industry/Entity Type

Real Estate

Font styles to use
Serif

Requirements
Must have
• Should be a serious, sophisticated design in colors that match the business cards we uploaded. Design needs to match the color and fonts in the attached business cards. Can use the same design for each company, just change logo and color.
Should not have
• Nothing quirky or cute.

```html
<!DOCTYPE html>
<html lang="en">
<head>
<meta charset="utf-8">
<title>Kestrel Row Construction Management – Letterhead</title>
<link rel="stylesheet" href="https://fonts.googleapis.com/css2?family=Cormorant+Garamond:wght@500;600;700&display=swap">
<style>
  :root {
    --gold: #b18a3f;
    --gold-deep: #9c7734;
    --ink: #3a3a3c;
    --paper: #ffffff;
    --band-text: #f6eedd;
  }
  * { margin: 0; padding: 0; box-sizing: border-box; }
  html, body { width: 849px; height: 1200px; overflow: hidden; background: var(--paper); }
  .letterhead {
    position: relative;
    width: 849px;
    height: 1200px;
    background: var(--paper);
    font-family: "Cormorant Garamond", Georgia, serif;
    color: var(--ink);
  }
  .brand {
    position: absolute;
    left: 44px;
    top: 40px;
    display: flex;
    align-items: center;
    gap: 12px;
  }
  .brand-mark {
    width: 34px;
    height: 34px;
    background: var(--gold);
  }
  .brand-name {
    font-weight: 600;
    font-size: 21px;
    line-height: 1.05;
    color: var(--gold);
    letter-spacing: 0.02em;
    text-transform: uppercase;
  }
  .contact {
    position: absolute;
    left: 42px;
    top: 1100px;
    font-size: 13px;
    line-height: 1.45;
    color: var(--ink);
  }
  .contact-phones { display: flex; gap: 22px; }
  .contact-phones span { display: inline-flex; align-items: center; gap: 5px; }
  .contact-phones svg { width: 9px; height: 9px; fill: var(--gold); }
  .contact-email { font-weight: 700; }
  .footer-band {
    position: absolute;
    left: 0;
    bottom: 0;
    width: 100%;
    height: 58px;
    background: linear-gradient(90deg, var(--gold-deep), var(--gold));
    padding: 12px 42px 0;
    color: var(--band-text);
    font-size: 13px;
    line-height: 1.4;
  }
  .footer-address { font-weight: 700; }
</style>
</head>
<body>
  <main class="letterhead">
    <header class="brand">
      <div class="brand-mark"></div>
      <div class="brand-name">Kestrel Row<br>Construction Management</div>
    </header>

    <section class="contact">
      <div class="contact-phones">
        <span><svg viewBox="0 0 10 10"><path d="M2 0h2l1 3-1.5 1a6 6 0 0 0 2.5 2.5L7 5l3 1v2c0 1-1 2-2 2A8 8 0 0 1 0 2c0-1 1-2 2-2z"/></svg>312.555.0148</span>
        <span><svg viewBox="0 0 10 10"><rect x="1" y="3" width="8" height="6" rx="1"/><rect x="3" y="0" width="4" height="3"/></svg>312.555.0149</span>
      </div>
      <div class="contact-email">office@kestrelrowbuild.com</div>
    </section>

    <footer class="footer-band">
      <div class="footer-web">www.kestrelrowbuild.com</div>
      <div class="footer-address">1480 W Larkin Ave, Chicago, IL 60622</div>
    </footer>
  </main>
</body>
</html>
```